Carpentry company Needs a business card design

We need a design for a Carpentry / building company, business card. Please think of designs out of the ordinary and try to make it eye catching. Our existing logo will need to be incorporated in the design. However feel free to change the colours of the logo to suit your design. I would like to see some designs with green /black and orange incorporated into it.These are not the only colours accepted and all designs that appeal will be accepted.

Please contact me should you have any questions
Thanks Marcus

Target Market(s)

General Public seeking carpentry work

Industry/Entity Type

Business

Contact Information for Business Card

- Current company logo ( colours can be changed)
-Phone number ,
- info@brantelworks.com.au
- brantelworks.com.au
-the facebook symbol

Font styles to use
Other font styles liked:
• You choose

Requirements
Must have
• Services we provide
• - Renovations
• -Deckings & Pergolas
• -Kitchens
• - Bathrooms
• - Intricate details
Nice to have
• an awesome design
Should not have
• Tools on the business card

```html
<!DOCTYPE html>
<html lang="en">
<head>
<meta charset="utf-8">
<title>Brantel Works – Business Card</title>
<link rel="stylesheet" href="https://fonts.googleapis.com/css2?family=Montserrat:wght@500;700&family=Open+Sans:wght@400;600&display=swap">
<style>
  :root {
    --backdrop: #3a322e;
    --card-white: #f4f4f2;
    --card-black: #1b1b1b;
    --band-black: #141414;
    --pattern-dark: #2c2c2c;
    --pattern-light: #4a4a4a;
    --ink: #2a2a2a;
    --orange: #e08a22;
    --white: #ffffff;
    --muted-white: #cfcfcf;
  }
  * { box-sizing: border-box; margin: 0; padding: 0; }
  html, body { width: 1200px; height: 716px; overflow: hidden; }
  body {
    background: var(--backdrop);
    position: relative;
    font-family: "Open Sans", Arial, sans-serif;
  }
  .card {
    position: absolute;
    top: 208px;
    width: 520px;
    height: 300px;
    border-radius: 4px;
    overflow: hidden;
  }
  /* Front */
  .card-front { left: 60px; background: var(--card-white); color: var(--ink); }
  .front-brand {
    position: absolute; right: 36px; top: 34px;
    display: flex; align-items: center; gap: 10px;
  }
  .brand-mark { width: 16px; height: 16px; background: var(--orange); flex: none; }
  .brand-name {
    font-family: "Montserrat", Arial, sans-serif; font-weight: 700;
    font-size: 30px; letter-spacing: 1px; color: var(--ink); line-height: 1;
    white-space: nowrap;
  }
  .front-rule {
    position: absolute; left: 0; top: 80px; width: 300px; height: 4px;
    background: var(--orange);
  }
  .holder { position: absolute; left: 30px; top: 96px; }
  .holder-name {
    font-family: "Montserrat", Arial, sans-serif; font-weight: 500;
    font-size: 20px; letter-spacing: 0.5px; text-transform: uppercase; line-height: 1.2;
  }
  .holder-name .surname { color: var(--orange); }
  .holder-role { font-size: 12px; color: var(--orange); margin-top: 2px; }
  .contact-list {
    position: absolute; right: 36px; top: 122px;
    list-style: none; text-align: right; font-size: 14px; line-height: 1.55;
  }
  .contact-list li { display: flex; justify-content: flex-end; align-items: center; gap: 8px; }
  .contact-icon { width: 14px; height: 14px; flex: none; }
  .contact-icon.blank { visibility: hidden; }
  /* Back */
  .card-back { left: 620px; background: var(--card-black); }
  .pattern-band {
    position: absolute; top: 0; width: 100px; height: 100%;
    background: linear-gradient(135deg, var(--pattern-light), var(--pattern-dark) 60%, var(--band-black));
  }
  .pattern-band.left { left: 0; }
  .pattern-band.right { right: 0; transform: scaleX(-1); }
  .back-centre {
    position: absolute; left: 100px; right: 100px; top: 0; bottom: 0;
    background: var(--band-black);
    display: flex; flex-direction: column; align-items: center; justify-content: center; gap: 18px;
  }
  .back-brand { display: flex; align-items: center; gap: 10px; }
  .back-brand .brand-mark { width: 14px; height: 14px; }
  .back-brand .brand-name { color: var(--white); font-size: 28px; }
  .service-list {
    list-style: none; display: flex; flex-wrap: wrap; justify-content: center;
    max-width: 290px; gap: 4px 12px;
    font-size: 11px; letter-spacing: 0.8px; text-transform: uppercase; color: var(--muted-white);
  }
  .service-list li { display: flex; align-items: center; gap: 6px; }
  .service-list li::before {
    content: ""; width: 5px; height: 5px; background: var(--orange); flex: none;
  }
</style>
</head>
<body>
  <section class="card card-front" aria-label="Business card front">
    <div class="front-brand">
      <span class="brand-mark"></span>
      <span class="brand-name">BRANTEL WORKS</span>
    </div>
    <div class="front-rule"></div>
    <div class="holder">
      <p class="holder-name">David <span class="surname">Marcus</span></p>
      <p class="holder-role">Director</p>
    </div>
    <ul class="contact-list">
      <li>0400 555 218
        <svg class="contact-icon" viewBox="0 0 14 14"><circle cx="7" cy="7" r="7" fill="#e08a22"/><path d="M4.5 3.5l1.5 0 .7 1.8-.9.7a5 5 0 0 0 2.2 2.2l.7-.9 1.8.7v1.5c-3.5.3-6.3-2.5-6-6z" fill="#fff"/></svg></li>
      <li>info@brantelworks.com.au
        <svg class="contact-icon" viewBox="0 0 14 14"><circle cx="7" cy="7" r="7" fill="#e08a22"/><rect x="3.5" y="4.5" width="7" height="5" fill="none" stroke="#fff" stroke-width="1"/><path d="M3.5 4.5L7 7.3l3.5-2.8" fill="none" stroke="#fff" stroke-width="1"/></svg></li>
      <li>www.brantelworks.com.au
        <svg class="contact-icon" viewBox="0 0 14 14"><circle cx="7" cy="7" r="7" fill="#e08a22"/><circle cx="7" cy="7" r="3.6" fill="none" stroke="#fff" stroke-width="1"/><path d="M3.4 7h7.2M7 3.4c-1.6 2-1.6 5.2 0 7.2M7 3.4c1.6 2 1.6 5.2 0 7.2" fill="none" stroke="#fff" stroke-width=".8"/></svg></li>
      <li>/brantelworks
        <svg class="contact-icon" viewBox="0 0 14 14"><circle cx="7" cy="7" r="7" fill="#e08a22"/></svg></li>
      <li>Consulting Rooms <svg class="contact-icon blank" viewBox="0 0 14 14"></svg></li>
      <li>42 Harwood Lane <svg class="contact-icon blank" viewBox="0 0 14 14"></svg></li>
      <li>Kelston VIC 3150 <svg class="contact-icon blank" viewBox="0 0 14 14"></svg></li>
    </ul>
  </section>

  <section class="card card-back" aria-label="Business card back">
    <div class="pattern-band left" role="img" aria-label="Glossy geometric cube pattern band"></div>
    <div class="back-centre">
      <div class="back-brand">
        <span class="brand-mark"></span>
        <span class="brand-name">BRANTEL WORKS</span>
      </div>
      <ul class="service-list">
        <li>Renovations</li>
        <li>Decking &amp; Pergolas</li>
        <li>Kitchens</li>
        <li>Bathrooms</li>
        <li>Intricate Details</li>
      </ul>
    </div>
    <div class="pattern-band right" role="img" aria-label="Glossy geometric cube pattern band"></div>
  </section>
</body>
</html>
```